Residential Roofing Company, need a Unique business card for a Woman owned ompany

Woman Owned Residential Roofing Company. Specializing in Insurance Claims
Attention to Detail is what sets this woman owned roofing company apart from the rest
We are QORVEL Certified and are an Accredited business with an A rating with the TMK. Our Contractor License number LTW38154

```html
<!DOCTYPE html>
<html lang="en">
<head>
<meta charset="utf-8">
<title>Harborcrest Roofing – Business Card</title>
<link rel="stylesheet" href="https://fonts.googleapis.com/css2?family=Montserrat:wght@600;700;800&family=Open+Sans:wght@400;600&display=swap">
<style>
  :root {
    --navy: #22306a;
    --navy-soft: #2f3f7c;
    --ink: #161a24;
    --paper: #ffffff;
    --backdrop: #3b3c40;
    --badge-blue: #1e6aa0;
  }
  * { box-sizing: border-box; margin: 0; padding: 0; }
  html, body { width: 1200px; height: 801px; overflow: hidden; }
  body {
    background: var(--backdrop);
    display: flex;
    align-items: center;
    justify-content: center;
    gap: 40px;
    font-family: "Open Sans", Arial, sans-serif;
  }
  .card {
    position: relative;
    width: 540px;
    height: 309px;
    border-radius: 18px;
    overflow: hidden;
    box-shadow: 0 10px 24px rgba(0,0,0,.35);
  }
  /* back side */
  .card--back {
    background: var(--navy);
    display: flex;
    align-items: center;
    justify-content: center;
  }
  .brand {
    display: flex;
    align-items: center;
    gap: 10px;
    font-family: "Montserrat", Arial, sans-serif;
    font-weight: 800;
    letter-spacing: .5px;
    white-space: nowrap;
  }
  .brand__mark { width: 16px; height: 16px; flex: none; }
  .card--back .brand { color: var(--navy-soft); font-size: 34px; }
  .card--back .brand__mark { background: var(--navy-soft); width: 22px; height: 22px; }
  /* front side */
  .card--front { background: var(--paper); color: var(--ink); }
  .wave { position: absolute; inset: 0; width: 100%; height: 100%; }
  .identity { position: absolute; left: 40px; top: 96px; }
  .identity__name {
    font-family: "Montserrat", Arial, sans-serif;
    font-weight: 700; font-size: 26px; line-height: 1.2; color: var(--navy);
  }
  .identity__title { font-size: 14px; font-weight: 600; margin-top: 2px; }
  .address { position: absolute; left: 80px; top: 160px; font-size: 14px; line-height: 1.4; }
  .contacts { position: absolute; left: 80px; top: 210px; list-style: none; font-size: 14px; line-height: 1.4; }
  .contacts li { display: flex; align-items: center; gap: 10px; }
  .contacts svg { width: 12px; height: 12px; fill: var(--ink); flex: none; }
  .logo-block { position: absolute; right: 26px; top: 28px; display: flex; flex-direction: column; align-items: center; }
  .card--front .brand { color: var(--navy); font-size: 22px; }
  .card--front .brand__mark { background: var(--navy); }
  .license { font-size: 11px; margin-top: 6px; border-top: 2px solid var(--navy); padding-top: 4px; align-self: stretch; text-align: center; }
  .badge {
    position: absolute; right: 46px; top: 144px;
    width: 140px; height: 54px; border-radius: 6px;
    background: var(--badge-blue);
    border: 2px solid var(--badge-blue);
    display: flex;
  }
  .badge__seal { width: 48px; background: var(--paper); border-radius: 4px 0 0 4px; }
</style>
</head>
<body>
  <section class="card card--back" aria-label="Card back">
    <div class="brand"><span class="brand__mark"></span>HARBORCREST ROOFING</div>
  </section>

  <section class="card card--front" aria-label="Card front">
    <svg class="wave" viewBox="0 0 540 309" preserveAspectRatio="none" aria-hidden="true">
      <path d="M540 150 C470 160 430 230 340 266 C290 286 230 300 190 309 L540 309 Z" fill="var(--navy)"/>
      <path d="M540 150 C470 160 430 230 340 266 C290 286 230 300 190 309" fill="none" stroke="var(--ink)" stroke-width="5"/>
      <path d="M540 157 C472 168 434 238 344 273 C296 292 240 303 210 309" fill="none" stroke="var(--paper)" stroke-width="3"/>
    </svg>

    <div class="identity">
      <h1 class="identity__name">Dana Whitfield</h1>
      <p class="identity__title">Chief Executive Officer</p>
    </div>

    <p class="address">48 Alder Lane<br>Westbrook MA 02190</p>

    <ul class="contacts">
      <li><svg viewBox="0 0 24 24"><path d="M6.6 10.8a15 15 0 0 0 6.6 6.6l2.2-2.2c.3-.3.7-.4 1-.2 1.1.4 2.300.6 3.6.6.6 0 1 .4 1 1V20c0 .6-.4 1-1 1A17 17 0 0 1 3 4c0-.6.4-1 1-1h3.5c.6 0 1 .4 1 1 0 1.3.2 2.5.6 3.6.1.3 0 .7-.2 1z"/></svg>555.014.2278</li>
      <li><svg viewBox="0 0 24 24"><path d="M7 1h10a2 2 0 0 1 2 2v18a2 2 0 0 1-2 2H7a2 2 0 0 1-2-2V3a2 2 0 0 1 2-2zm0 4v13h10V5z"/></svg>555.019.4630</li>
      <li><svg viewBox="0 0 24 24"><path d="M2 5h20v14H2zm2 2v.5l8 5 8-5V7z"/></svg>dana@harborcrestroof.com</li>
      <li><svg viewBox="0 0 24 24"><circle cx="12" cy="12" r="10"/></svg>www.harborcrestroof.com</li>
    </ul>

    <div class="logo-block">
      <div class="brand"><span class="brand__mark"></span>HARBORCREST ROOFING</div>
      <p class="license">Contractor License number LTW38154</p>
    </div>

    <div class="badge" role="img" aria-label="TMK accredited business badge">
      <span class="badge__seal"></span>
    </div>
  </section>
</body>
</html>
```